Mother's Day and Baby Blessing poster

I need a poster Mother's Day and Baby Blessing ceremony for a Marigold Lights Festival at Sydney Wattlebrook Quay. There is no specification on the design, however the only require is to present mother and baby. I would like the design to be modern and simple.

Please refer to the past years design (however I hope it to have a different feel to the past) http://marigoldlightsfest.com.au/event/details/baby-blessing-ceremony/.

Baby

• Date: 7/5/2017 (Sunday)
• Time: 1:30pm (12:30pm registration)
• Venue: Yarrowdene Park, Wattlebrook Quay

```html
<!DOCTYPE html>
<html lang="en">
<head>
<meta charset="utf-8">
<title>Mother's Day &amp; Baby Blessing Ceremony</title>
<link href="https://fonts.googleapis.com/css2?family=Arimo:wght@400;700&display=swap" rel="stylesheet">
<style>
  :root {
    --backdrop: #000000;
    --peach: #fadba3;
    --ink: #1a1418;
    --paper: #ffffff;
    --rose: #e88082;
    --denim: #1e6b9c;
  }
  html, body {
    margin: 0;
    padding: 0;
    width: 1200px;
    height: 1200px;
    overflow: hidden;
    background: var(--backdrop);
  }
  .poster {
    position: absolute;
    left: 268px;
    top: 88px;
    width: 694px;
    height: 982px;
    background: var(--peach);
    overflow: hidden;
    font-family: "Arimo", Arial, sans-serif;
    color: var(--ink);
  }
  .waves {
    position: absolute;
    inset: 0;
  }
  .mother-and-baby {
    position: absolute;
    left: 236px;
    top: 128px;
    width: 340px;
    height: 580px;
    border-radius: 170px 170px 40px 40px;
    background: linear-gradient(165deg, #1a1418 0%, #1a1418 20%, #ffffff 32%, #e88082 58%, #1e6b9c 100%);
  }
  .title {
    position: absolute;
    top: 32px;
    left: 0;
    width: 100%;
    margin: 0;
    text-align: center;
    font-weight: 700;
    font-size: 33px;
    line-height: 41px;
    letter-spacing: 0.5px;
  }
  .when {
    position: absolute;
    left: 30px;
    margin: 0;
    font-weight: 700;
    line-height: 1;
    white-space: nowrap;
  }
  .when-day { top: 732px; font-size: 44px; letter-spacing: 1px; }
  .when-date { top: 782px; font-size: 60px; letter-spacing: 1px; }
  .when-time { top: 852px; font-size: 40px; }
  .when-time .onwards { font-size: 24px; letter-spacing: 1px; }
  .registration { top: 906px; left: 36px; font-size: 16px; letter-spacing: 0.8px; }
  .venue {
    position: absolute;
    left: 36px;
    top: 936px;
    margin: 0;
    font-weight: 700;
    font-size: 24px;
    letter-spacing: 1.2px;
    line-height: 1;
    white-space: nowrap;
  }
  .festival-name {
    position: absolute;
    left: 424px;
    top: 836px;
    width: 244px;
    margin: 0;
    text-align: right;
    font-weight: 700;
    font-size: 26px;
    line-height: 30px;
    color: var(--ink);
  }
</style>
</head>
<body>
  <main class="poster">
    <svg class="waves" width="694" height="982" viewBox="0 0 694 982" aria-hidden="true">
      <path fill="var(--paper)" d="M0,596 C80,578 240,610 320,800 L400,824 C500,760 600,740 694,750 L694,982 L0,982 Z"/>
    </svg>

    <div class="mother-and-baby" role="img" aria-label="Illustration of a smiling mother in a pink shirt holding her baby in blue trousers, the baby's hands pressed together in prayer"></div>

    <h1 class="title">MOTHER'S DAY &amp; BABY BLESSING<br>CEREMONY</h1>

    <p class="when when-day">SUNDAY</p>
    <p class="when when-date">07.05.2017</p>
    <p class="when when-time">1.30 PM <span class="onwards">ONWARDS</span></p>
    <p class="when registration">12.30 PM FOR REGISTRATION</p>
    <p class="venue">YARROWDENE PARK, WATTLEBROOK QUAY</p>

    <p class="festival-name">Marigold Lights<br>Festival</p>
  </main>
</body>
</html>
```